Strong Pulse, Clear Mind Poster for American Indian Older Adults

We need am 11" x 17" poster designed for a health outreach project designed to reach older U.S. American Indians. The materials developed through this project will be distributed to American Indian and Alaska Native tribes, communities and tribal-serving organizations across the U.S. (more than 500 different tribes). If we find a successful design we will work with that designer to produce at least one other item we need design work for using the same look/feel and maybe other materials for this project. (more work!). The poster will include a set of facts (bulleted list on the attached document) that we would like presented in an "infographic" style. The design must be reflective of the American Indian culture and designed with older adults (65 and older) in mind. Imagery plays a strong role in the American Indian culture in the U.S. images of the heart, water, feathers, circle of life, etc. If you use photos of people they must include older adults and they must be American Indian (Native American). We prefer deep earth tones for the color scheme. The design must take into account design principles for older adults: 1. Try not to put colored font on colored background 2. Ensure high contrast for text 3. Font style should be sans serif, not cursive,decorative or heavily stylized because it is harder to read 4. Avoid using all caps 5. Don't print sideways or on top of images, shaded, backgrounds, etc. 6. All images should related specifically to the content of the text and be culturally appropriate for both older adults and American Indians. The final design should be easy to read and appeal to older American Indian adults. We need to incorporate three logos on the poster towards the bottom they should not be the center/focus of the poster. We also need to include a statement about who produced the materials- that can be very small below the logos at the bottom of the poster. We've attached the text for the poster and three logo files (note one is solid blue- we will finalize that after the document design is selected but need a placeholder for that logo.

Target Market(s)

Older adult (65 and older) American Indian and Alaska Natives and their family members in tribes, communities and tribal-serving organizations across the US

Font styles to use
Sans Serif

Requirements
Must have
• Must adhere to good design principles for older adults (listed in project description)
• Must feature culturally appropriate/targeted imagery and design look and feel

```html
<!DOCTYPE html>
<html lang="en">
<head>
<meta charset="utf-8">
<title>Strong Pulse, Clear Mind</title>
<link rel="stylesheet" href="https://fonts.googleapis.com/css2?family=Barlow+Condensed:wght@400;500&family=Fira+Sans:wght@400;500;700;800&display=swap">
<style>
  :root {
    --frame: #8e3a1f;
    --frame-deep: #5a2614;
    --paper: #fbf6ee;
    --ink: #2b1a10;
    --headline: #8e3a1f;
    --sage: #6f7d3c;
    --turquoise: #2e7f7d;
    --terracotta: #a9482c;
    --ochre: #c58a2a;
    --badge: #dcc7a8;
    --image-light: #d9a46a;
    --image-dark: #7a3a1e;
  }
  * { margin: 0; padding: 0; box-sizing: border-box; }
  html, body { width: 901px; height: 1200px; overflow: hidden; background: var(--frame); }
  .poster {
    position: relative;
    width: 901px;
    height: 1200px;
    background: var(--frame);
    font-family: "Fira Sans", Arial, sans-serif;
    color: var(--ink);
  }
  .poster__rule {
    position: absolute;
    left: 20px; top: 19px; right: 20px; bottom: 19px;
    border: 2px solid var(--paper);
  }
  .poster__panel {
    position: absolute;
    left: 41px; top: 36px;
    width: 819px; height: 814px;
    background: var(--paper);
  }
  .headline {
    position: absolute;
    left: 28px; top: 14px;
    color: var(--headline);
    font-weight: 800;
    font-size: 80px;
    line-height: 82px;
  }
  .tagline {
    position: absolute;
    left: 31px; top: 200px;
    font-family: "Barlow Condensed", "Arial Narrow", sans-serif;
    font-weight: 500;
    font-size: 43px;
    line-height: 52px;
  }
  .feature-image {
    position: absolute;
    left: 445px; top: 190px;
    width: 345px; height: 230px;
    border-radius: 16px;
    background: radial-gradient(ellipse at 45% 40%, var(--image-light) 0%, #b0643a 55%, var(--image-dark) 100%);
  }
  .facts {
    position: absolute;
    left: 0; top: 0;
    width: 819px; height: 814px;
  }
  .fact-list {
    position: absolute;
    left: 30px; top: 655px;
    width: 765px;
    display: flex;
    gap: 15px;
    list-style: none;
  }
  .fact-list__item {
    width: 180px;
    text-align: center;
    font-weight: 500;
    font-size: 19px;
    line-height: 25px;
  }
  .risk-band {
    position: absolute;
    left: 0; top: 864px;
    width: 901px;
    text-align: center;
    color: var(--paper);
    font-weight: 500;
    font-size: 25px;
    line-height: 29px;
  }
  .call-to-action {
    position: absolute;
    left: 41px; top: 964px;
    width: 819px; height: 116px;
    background: var(--paper);
    display: flex;
    align-items: center;
    justify-content: center;
    text-align: center;
    font-weight: 500;
    font-size: 28px;
    line-height: 35px;
  }
  .call-to-action strong { font-weight: 800; color: var(--frame-deep); }
  .partners {
    position: absolute;
    left: 41px; top: 1092px;
    width: 819px; height: 89px;
    background: var(--paper);
    display: flex;
    flex-direction: column;
    align-items: center;
    justify-content: center;
    gap: 8px;
  }
  .partners__logos {
    display: flex;
    gap: 40px;
  }
  .partners__badge {
    width: 130px; height: 42px;
    border-radius: 6px;
    background: var(--badge);
  }
  .partners__credit {
    font-size: 14px;
    line-height: 18px;
  }
</style>
</head>
<body>
<main class="poster">
  <div class="poster__rule"></div>

  <section class="poster__panel">
    <h1 class="headline">Strong Pulse,<br>Clear Mind...</h1>

    <p class="tagline">The River of Life Flows<br>Through the Heart,<br>Protecting the Mind<br>and Body</p>

    <div class="feature-image" role="img" aria-label="Heart with flowing water and a feather in a circle of life, in warm earth tones"></div>

    <svg class="facts" viewBox="0 0 819 814" xmlns="http://www.w3.org/2000/svg" aria-hidden="true">
      <polygon fill="var(--sage)" points="120,540 50,600 84,600 84,640 156,640 156,600 190,600"/>
      <polygon fill="var(--turquoise)" points="315,515 245,575 279,575 279,640 351,640 351,575 385,575"/>
      <polygon fill="var(--terracotta)" points="510,490 440,550 474,550 474,640 546,640 546,550 580,550"/>
      <polygon fill="var(--ochre)" points="705,465 635,525 669,525 669,640 741,640 741,525 775,525"/>
      <rect x="30" y="640" width="765" height="3" fill="var(--frame-deep)"/>
    </svg>

    <ul class="fact-list">
      <li class="fact-list__item">5.7 million Americans have Alzheimer’s disease</li>
      <li class="fact-list__item">Alzheimer’s is the 6th leading cause of death</li>
      <li class="fact-list__item">1 out of 10 people age 65 and older has Alzheimer’s</li>
      <li class="fact-list__item">1 out of 3 American Indians over 65 develop dementia, including Alzheimer’s</li>
    </ul>
  </section>

  <p class="risk-band">Elders with diabetes, heart disease,<br>or high blood pressure have a much higher risk<br>of developing Alzheimer’s or other dementias</p>

  <section class="call-to-action">
    <p>Make an <strong>appointment</strong> with your doctor<br><strong>today</strong> to talk about how to<br>keep your mind and <strong>heart healthy.</strong></p>
  </section>

  <footer class="partners">
    <div class="partners__logos">
      <div class="partners__badge" role="img" aria-label="Partner logo"></div>
      <div class="partners__badge" role="img" aria-label="Partner logo"></div>
      <div class="partners__badge" role="img" aria-label="Partner logo"></div>
    </div>
    <p class="partners__credit">Produced by the Elder Wellness Outreach Project</p>
  </footer>
</main>
</body>
</html>
```